Remote Computer Support PostCard

We need a Postcard Ad for marketing to businesses that need Remote Computer Support and Security. 2 sided and able to be mailed. Can be any color but color we use mostly is red. Remote Computer Support and Security per PC. Includes Remote Monitoring and Maintenance(RMM) Agent, Business Security Tools including Antivirus, Anti Malware, Ransomware Protection, Intrusion Prevention, Content Filtering and others. All remote support you need for $69.99 per pc per month.

Target Market(s)

All Businesses

Industry/Entity Type

Computer Support for Businesses

Colors
EB3D1F
EC4F4E
F09395
F8D3D4
FCEDEE

Requirements
Must have
• Bytharo, Inc. (555) 314-2968 . Sales@bytharo-example.com. Designed to be mailed. 6x9 Postcard Mailer Size Final 6.25" x 9" Ink & Bleed Four Color Process, Full Bleed Two Sides. Must have places for postage.
Nice to have
• Main lines should be in top 1/3 of postcard to stand out in mail.

```html
<!DOCTYPE html>
<html lang="en">
<head>
<meta charset="utf-8">
<title>Bytharo, Inc. – Postcard Back</title>
<link rel="stylesheet" href="https://fonts.googleapis.com/css2?family=Nunito:wght@800;900&family=Questrial&display=swap">
<style>
  :root {
    --red: #d62028;
    --red-dark: #a81a22;
    --charcoal: #3f3f3f;
    --ink: #1e1e1e;
    --paper: #ffffff;
    --heading: "Nunito", sans-serif;
    --body: "Questrial", sans-serif;
  }
  * { margin: 0; padding: 0; box-sizing: border-box; }
  html, body { width: 1200px; height: 811px; overflow: hidden; background: var(--paper); }
  .postcard { position: relative; width: 1200px; height: 811px; overflow: hidden; background: var(--paper); font-family: var(--body); color: var(--ink); }
  .shapes { position: absolute; inset: 0; }

  .service { position: absolute; left: 151px; width: 620px; }
  .service h2 { font-family: var(--heading); font-weight: 900; font-size: 21.8px; line-height: 28px; letter-spacing: 0.1px; color: var(--ink); white-space: nowrap; }
  .service p { margin-left: 5px; font-size: 18px; line-height: 21.7px; color: var(--ink); white-space: nowrap; }
  .service--rmm { top: 66px; }
  .service--desk { top: 164px; }
  .service--security { top: 261px; }

  .stamp-box { position: absolute; left: 966px; top: 51px; width: 182px; height: 182px; border: 1.6px solid var(--ink); }
  .address-line { position: absolute; left: 749px; width: 389px; height: 52px; border: 1.6px solid var(--ink); }
  .address-line--1 { top: 279px; }
  .address-line--2 { top: 362px; }
  .address-line--3 { top: 446px; }

  .about { position: absolute; left: 75px; top: 464px; width: 460px; color: var(--paper); }
  .about h3 { font-family: var(--heading); font-weight: 900; font-size: 28px; line-height: 34px; padding-left: 14px; }
  .about .rule { width: 91px; height: 3.5px; background: var(--paper); margin-top: 2px; margin-bottom: 12px; }
  .about p { font-size: 17.2px; line-height: 21.7px; }
  .about p + p { margin-top: 21.7px; }
  .about .line { display: block; white-space: nowrap; }
  .about .line--spread { white-space: normal; text-align: justify; text-align-last: justify; }

  .contact { position: absolute; color: var(--paper); white-space: nowrap; }
  .contact-email { left: 827px; top: 614px; font-size: 25px; line-height: 32px; }
  .contact-cta { left: 835px; top: 686px; font-family: var(--heading); font-weight: 900; font-size: 21px; line-height: 24px; letter-spacing: 0.5px; }
  .contact-phone { left: 833px; top: 708px; font-family: var(--heading); font-weight: 900; font-size: 40px; line-height: 48px; letter-spacing: 0.5px; }
  .phone-icon { position: absolute; left: 766px; top: 699px; width: 42px; height: 44px; }
</style>
</head>
<body>
<div class="postcard">
  <svg class="shapes" width="1200" height="811" viewBox="0 0 1200 811" aria-hidden="true">
    <path d="M 93 94.5 H 74.5 V 295 H 93" fill="none" stroke="var(--red)" stroke-width="5"/>
    <g id="badge">
      <polygon points="115.7,68.6 140.7,83 140.7,111 115.7,125.4 90.7,111 90.7,83" fill="var(--red)"/>
      <polygon points="115.7,68.6 140.7,83 140.7,111 115.7,125.4" fill="var(--red-dark)"/>
      <path d="M115.7 80.5 L128.5 85.5 V97 C128.5 104 123 109 115.7 113 C108.4 109 102.9 104 102.9 97 V85.5 Z" fill="none" stroke="var(--paper)" stroke-width="2"/>
      <path d="M115.7 84.5 L125 88.2 V97 C125 102 121 105.8 115.7 108.7 C110.4 105.8 106.4 102 106.4 97 V88.2 Z" fill="none" stroke="var(--paper)" stroke-width="1.2"/>
      <circle cx="115.7" cy="96.5" r="4" fill="none" stroke="var(--paper)" stroke-width="1.4"/>
      <path d="M110 93 L112 94.5 M121.4 93 L119.4 94.5 M110 100 L112 98.5 M121.4 100 L119.4 98.5 M115.7 90 V92.5" stroke="var(--paper)" stroke-width="1.2"/>
    </g>
    <use href="#badge" y="98.1"/>
    <use href="#badge" y="195.4"/>

    <line x1="27" y1="419" x2="226" y2="358" stroke="var(--red)" stroke-width="4.5"/>
    <polygon points="361.5,344.5 49.6,439.5 0,656 0,779 33.6,811 543.8,811 599.6,566.5" fill="var(--charcoal)"/>
    <polyline points="453,409.5 630,572 609.4,661" fill="none" stroke="var(--ink)" stroke-width="4.8"/>
    <polygon points="537.6,460 595.4,460 679,538.6 1200,538.6 1200,811 605,811 659,574" fill="var(--red)"/>
  </svg>

  <section class="service service--rmm">
    <h2>Remote Monitoring and Management Agent (RMM)</h2>
    <p>Lorem ipsum dolor sit amet, consectetuer adipiscing elit, sed diam<br>nonummy nibh euismod</p>
  </section>
  <section class="service service--desk">
    <h2>Help Desk Application on Desktop</h2>
    <p>Lorem ipsum dolor sit amet, consectetuer<br>adipiscing elit, sed diam nonummy nibh euismod</p>
  </section>
  <section class="service service--security">
    <h2>Vantorix Steady Guard Business Security</h2>
    <p>Lorem ipsum dolor sit amet, consectetuer<br>adipiscing elit, sed diam nonummy nibh euismod</p>
  </section>

  <div class="stamp-box"></div>
  <div class="address-line address-line--1"></div>
  <div class="address-line address-line--2"></div>
  <div class="address-line address-line--3"></div>

  <section class="about">
    <h3>About us</h3>
    <div class="rule"></div>
    <p>
      <span class="line line--spread" style="width:386px">Lorem ipsum dolor sit amet, consectetuer</span>
      <span class="line line--spread" style="width:409px">adipiscing elit, sed diam nonummy nibh euismod</span>
      <span class="line line--spread" style="width:430px">tincidunt ut is so too laoreet dolore magna aliquam</span>
      <span class="line">erat volutpat.</span>
    </p>
    <p>
      <span class="line">Ut wisi enim ad minim veniam, quis nostrud exerci tation</span>
      <span class="line line--spread" style="width:443px">ullamcorper suscipit lobortis nisl ut aliquip ex ea</span>
      <span class="line">commodo conse. Duis autem vel eum iriure dolor in at,</span>
      <span class="line">vel illum dolore eu feugiat nulla facilisis at vero eros et</span>
      <span class="line">accumsan et iusto odio dignissim qui blandit praesent</span>
      <span class="line">luptatum zzril delenit augue duis</span>
    </p>
  </section>

  <div class="contact contact-email">Sales@bytharo-example.com</div>
  <svg class="phone-icon" viewBox="0 0 42 44" aria-hidden="true">
    <path d="M6 12 C4 18 8 28 16 35 C22 40 28 42 31 40 L34 36 C35 34.5 34.5 33 33 32 L27 28.5 C25.5 27.8 24 28 23 29.5 L21.5 31.5 C17.5 29.5 13.5 25 11.5 21 L13.5 19.5 C15 18.5 15.3 17 14.5 15.5 L11 9.5 C10 8 8.5 7.5 7 8.5 Z" fill="var(--paper)"/>
    <path d="M20 12 A9 9 0 0 1 29 21" fill="none" stroke="var(--paper)" stroke-width="2"/>
    <path d="M20 6.5 A14.5 14.5 0 0 1 34.5 21" fill="none" stroke="var(--paper)" stroke-width="2"/>
    <path d="M20 1.5 A19.5 19.5 0 0 1 39.5 21" fill="none" stroke="var(--paper)" stroke-width="2"/>
  </svg>
  <div class="contact contact-cta">CALL FOR MORE INFO</div>
  <div class="contact contact-phone">(555) 314-2968</div>
</div>
</body>
</html>
```